LUMO Electrical Services Letter Head

I need a professional clean looking design that will incorporate my company logo and information such as postal address, website, contact email "service@lumoelectrical.com.au" and phone number.

somewhere on the document i will also require my electrical contractor number "EC 047362" and my Australian Business number "57 193 640 208" these have to legally be on the document so they dont need to be a main feature, maybe in the footer in a smaller text.

Can you also have the 3 blue dashes from my logo as the watermark.

I would like the colour scheme to match my logo, business card and website www.lumoelectrical.com.au

I have the JPEG and PNG files for my logo which it will not allow me to upload as they are too wide, if you require these please let me know.

Target Market(s)

To be used for quotes and letters to commercial clients

Industry/Entity Type

Electric Company

Colors
0555a3
3176b5
85acd3
cfdfed
eaf1f7

Requirements
Must have
• company logo and information such as postal address, website, contact email "service@lumoelectrical.com.au" and phone number.
• somewhere on the document i will also require my electrical contractor number "EC 047362" and my Australian Business number "57 193 640 208" these have to legally be on the document so they dont need to be a main feature, maybe in the footer in a smaller text.
• I would like the colour scheme to match my logo, business card and website www.lumoelectrical.com.au
Nice to have
• Can you also have the 3 blue dashes from my logo as the watermark.

```html
<!DOCTYPE html>
<html lang="en">
<head>
<meta charset="utf-8">
<title>LUMO Electrical Services – Letterhead</title>
<link href="https://fonts.googleapis.com/css2?family=Open+Sans:wght@400;700&display=swap" rel="stylesheet">
<style>
  :root {
    --ink: #111111;
    --text: #555555;
    --rule: #c4c4c4;
    --blue-deep: #0e76bc;
    --blue-mid: #25a9e0;
    --band: #231f20;
    --paper-top: #ffffff;
    --paper-bottom: #f1f2f4;
  }
  * { margin: 0; padding: 0; box-sizing: border-box; }
  html, body { width: 933px; height: 1200px; overflow: hidden; background: #ffffff; }
  body { font-family: "Open Sans", Arial, sans-serif; }

  .letterhead {
    position: relative;
    width: 933px;
    height: 1200px;
    background: linear-gradient(135deg, var(--paper-top) 35%, var(--paper-bottom) 100%);
  }

  .brand {
    position: absolute;
    left: 30px;
    top: 50px;
    display: flex;
    align-items: center;
    gap: 12px;
  }
  .brand-square { width: 22px; height: 22px; background: var(--blue-deep); }
  .brand-name {
    font-size: 30px;
    font-weight: 700;
    color: var(--ink);
    letter-spacing: 0.2px;
  }

  .legal {
    position: absolute;
    left: 591px;
    top: 52px;
    height: 52px;
    padding-left: 15px;
    border-left: 1px solid var(--rule);
    font-size: 15px;
    line-height: 24px;
    color: var(--text);
  }

  .contact {
    position: absolute;
    left: 20px;
    top: 1097px;
    font-size: 15px;
    line-height: 24px;
    color: var(--text);
  }
  .contact-row { display: flex; align-items: center; gap: 12px; }
  .contact-item { display: inline-flex; align-items: center; gap: 5px; }
  .contact-item svg { width: 15px; height: 15px; fill: var(--blue-deep); }

  .footer-band {
    position: absolute;
    left: 0;
    bottom: 0;
    width: 933px;
    height: 50px;
    background: var(--band);
    display: flex;
    align-items: center;
    padding-left: 27px;
    gap: 9px;
    color: #ffffff;
    font-size: 15px;
  }
  .footer-band svg { width: 18px; height: 18px; }
</style>
</head>
<body>
<main class="letterhead">
  <header>
    <div class="brand">
      <span class="brand-square"></span>
      <span class="brand-name">LUMO Electrical Services</span>
    </div>
    <div class="legal">
      <p>LUMO Electrical Services | EC 047362</p>
      <p>Australian Business Number : 57 193 640 208</p>
    </div>
  </header>

  <footer>
    <div class="contact">
      <div class="contact-row">
        <span class="contact-item">
          <svg viewBox="0 0 16 16" aria-hidden="true"><path d="M8 0a8 8 0 1 0 0 16A8 8 0 0 0 8 0zm0 1.6a6.4 6.4 0 1 1 0 12.8A6.4 6.4 0 0 1 8 1.6zM6.2 4.2 5 5c-.4.3-.5.9-.3 1.4.8 1.7 2 3 3.6 3.9.5.3 1.1.2 1.4-.2l.9-1.1-1.6-1.1-.7.6c-.9-.5-1.6-1.2-2.1-2.1l.6-.7z"/></svg>
          (08) 6041 2759
        </span>
      </div>
      <div class="contact-row">
        <span class="contact-item">
          <svg viewBox="0 0 16 16" aria-hidden="true"><path d="M8 1 0 6v9h16V6zm0 2 5.6 3.5L8 10 2.4 6.5zM1.6 8l6.4 4 6.4-4v5.4H1.6z"/></svg>
          service@lumoelectrical.com.au
        </span>
        <span class="contact-item">
          <svg viewBox="0 0 16 16" aria-hidden="true"><path d="M8 0a8 8 0 1 0 0 16A8 8 0 0 0 8 0zm5.9 7.3h-2.6a12 12 0 0 0-.9-4.6 6.4 6.4 0 0 1 3.5 4.6zM8 1.7c.8 1 1.6 3 1.7 5.6H6.3C6.4 4.7 7.2 2.7 8 1.7zM5.6 2.7a12 12 0 0 0-.9 4.6H2.1a6.4 6.4 0 0 1 3.5-4.6zM2.1 8.7h2.6c.1 1.8.4 3.3.9 4.6a6.4 6.4 0 0 1-3.5-4.6zM8 14.3c-.8-1-1.6-3-1.7-5.6h3.4c-.1 2.6-.9 4.6-1.7 5.6zm2.4-1c.5-1.3.8-2.8.9-4.6h2.6a6.4 6.4 0 0 1-3.5 4.6z"/></svg>
          www.lumoelectrical.com.au
        </span>
      </div>
    </div>

    <div class="footer-band">
      <svg viewBox="0 0 18 18" aria-hidden="true"><circle cx="9" cy="9" r="9" fill="#ffffff"/><path d="M9 3.5a3.6 3.6 0 0 0-3.6 3.6c0 2.6 3.6 6.6 3.6 6.6s3.6-4 3.6-6.6A3.6 3.6 0 0 0 9 3.5zm0 5a1.4 1.4 0 1 1 0-2.8 1.4 1.4 0 0 1 0 2.8z" fill="#231f20"/></svg>
      <span class="address">P.O Box 8213, Harbourview East, WA 6158</span>
    </div>
  </footer>
</main>
</body>
</html>
```